Save The Date for 2019 QRP Symposium

We have an annual meeting each June and need a Save the Date (STD) designed. It should be a two-sided postcard with room for address and stamp (according to US Mail postal standards). I have attached some examples from prior years, but we would appreciate a more modern and attractive design for this year's STD.

Target Market(s)

Our own members - nurses, nurse practitioners, PAs and physicians

Industry/Entity Type

Medical

Requirements
Must have
• Must include our logos (attached), ideally in a coordinating fashion - as was done in prior years (see examples attached) and without modifying the logos too much. Needs have the following information:
• - "Save the Date"
• - "The 12th Annual Vascular Crew Roundtable"
• - "Friday, June 7, 2019" or "6/7/19"
• - "The Halvern–Trask Building | 274 West 19th Street | NYC"
• - Please include our website (www.zq-olm.example/events), phone number (212-555-0147) and email address (ask@zq-olm.example) for people to ask questions
• - Must have space for a postage stamp and the name/address of the postcard recipient
Nice to have
• Would be nice to remain in our blue/grey/olive color palate (see attached Brand Standards guide).
Should not have
• Please do not use stock photos of medical staff. Please don't use cartoons or cartoon images (although a tasteful sketch may be considered).

```html
<!DOCTYPE html>
<html lang="en">
<head>
<meta charset="utf-8">
<title>Save the Date – 12th Annual Vascular Crew Roundtable</title>
<link rel="stylesheet" href="https://fonts.googleapis.com/css2?family=Montserrat:ital,wght@0,400;0,500;0,600;0,700;0,800;1,800&family=Oswald:wght@600&display=swap">
<style>
  :root {
    --navy: #0b3f7a;
    --navy-deep: #0a3568;
    --sky: #2a7fc4;
    --sky-soft: #d7ebf8;
    --mist: #eef6fc;
    --white: #ffffff;
    --stamp: #e6e6e6;
    --rule: #9a9a9a;
    --page: #f2f2f0;
  }
  * { box-sizing: border-box; margin: 0; padding: 0; }
  html, body { width: 1200px; height: 1200px; overflow: hidden; background: var(--page); }
  body { position: relative; font-family: "Montserrat", Arial, sans-serif; }

  .postcard { position: absolute; width: 676px; height: 476px; overflow: hidden; box-shadow: 0 6px 18px rgba(0,0,0,.18); }
  .postcard--front { left: 263px; top: 87px; background: var(--white); }
  .postcard--back { left: 282px; top: 663px; background: var(--white); }

  .front-art { position: absolute; inset: 0; }
  .heart-sketch {
    position: absolute; left: 37px; top: 26px; width: 212px; height: 291px;
    border-radius: 40% 45% 48% 42%;
    background: radial-gradient(circle at 45% 45%, #c9d6e6 0%, #6f8db4 55%, var(--navy) 100%);
  }
  .headline { position: absolute; left: 250px; width: 400px; top: 22px; text-align: center; color: var(--navy); }
  .headline__title { font-weight: 800; font-size: 41px; letter-spacing: 1px; line-height: 1; }
  .headline__edition { font-weight: 800; font-style: italic; font-size: 23px; margin-top: 16px; }
  .headline__event { font-family: "Oswald", "Arial Narrow", sans-serif; font-weight: 600; font-size: 21px; color: var(--sky); margin-top: 8px; letter-spacing: .3px; }
  .headline__date { font-weight: 700; font-size: 24px; margin-top: 8px; letter-spacing: .5px; }
  .headline__venue { font-weight: 600; font-size: 15px; line-height: 20px; color: var(--navy); margin-top: 12px; }
  .headline__url { font-weight: 700; font-size: 15.5px; margin-top: 13px; }

  .front-contact { position: absolute; left: 38px; top: 390px; color: var(--white); font-size: 15.5px; line-height: 20px; font-weight: 500; }
  .partner-row { position: absolute; left: 302px; top: 402px; display: flex; align-items: center; gap: 26px; }
  .partner-badge { width: 54px; height: 54px; border-radius: 50%; border: 2px solid var(--white); }
  .chapter-name { display: flex; align-items: center; color: var(--white); }
  .chapter-name__rule { width: 1.5px; height: 40px; background: var(--white); margin-right: 12px; }
  .chapter-name__title { font-size: 20px; font-weight: 500; line-height: 1.1; }
  .chapter-name__sub { font-size: 9px; font-weight: 500; letter-spacing: 1px; margin-top: 2px; }

  .back-art { position: absolute; inset: 0; }
  .back-brand { position: absolute; left: 40px; top: 16px; display: flex; align-items: center; gap: 10px; color: var(--white); }
  .back-brand .partner-badge { width: 60px; height: 60px; }
  .back-copy {
    position: absolute; left: 36px; top: 100px; width: 248px; color: var(--white);
    font-size: 10.4px; line-height: 13.6px; text-align: justify;
  }
  .back-copy p + p { margin-top: 13.6px; }
  .back-url {
    position: absolute; left: 46px; top: 421px; width: 248px; height: 28px; border-radius: 14px;
    background: var(--white); color: var(--navy); font-size: 12px; text-align: center; line-height: 28px;
  }
  .stamp-box { position: absolute; left: 567px; top: 14px; width: 64px; height: 85px; background: var(--stamp); }
  .address-line { position: absolute; left: 374px; width: 267px; height: 1.5px; background: var(--rule); }
</style>
</head>
<body>

<section class="postcard postcard--front" aria-label="Postcard front">
  <svg class="front-art" width="676" height="476" viewBox="0 0 676 476" aria-hidden="true">
    <path d="M0 240 C160 290 360 230 676 150 L676 330 C470 380 250 360 0 300 Z" fill="var(--mist)"/>
    <path d="M0 280 C200 320 420 260 676 200 L676 340 C460 385 240 370 0 318 Z" fill="var(--sky-soft)"/>
    <path d="M0 321 C180 360 330 392 420 388 C520 384 600 368 676 349 L676 476 L0 476 Z" fill="var(--navy)"/>
  </svg>
  <div class="heart-sketch" role="img" aria-label="Engraved-style sketch of a human heart in navy ink"></div>

  <div class="headline">
    <h1 class="headline__title">SAVE THE DATE</h1>
    <p class="headline__edition">THE 12th ANNUAL</p>
    <p class="headline__event">VASCULAR CREW ROUNDTABLE</p>
    <p class="headline__edition" style="margin-top:6px">&amp; 2nd ANNUAL</p>
    <p class="headline__event">ZQOLM SUMMER SOIRÈE</p>
    <p class="headline__date">FRIDAY, JUNE 7, 2019</p>
    <p class="headline__venue">The Halvern–Trask Building<br>274 West 19th Street | NYC</p>
    <p class="headline__url">www.ZQ-OLM.example/12thAnnualQRP</p>
  </div>

  <p class="front-contact">For additional information<br>call (212) 555-0147 or<br>email ask@zq-olm.example</p>

  <div class="partner-row">
    <span class="partner-badge"></span>
    <span class="partner-badge"></span>
    <span class="partner-badge"></span>
    <div class="chapter-name">
      <span class="chapter-name__rule"></span>
      <div>
        <p class="chapter-name__title">Eastfield State</p>
        <p class="chapter-name__sub">CHAPTER</p>
      </div>
    </div>
  </div>
</section>

<section class="postcard postcard--back" aria-label="Postcard back">
  <svg class="back-art" width="676" height="476" viewBox="0 0 676 476" aria-hidden="true">
    <path d="M0 0 L406 0 C370 90 340 300 350 476 L0 476 Z" fill="var(--sky)"/>
    <path d="M0 0 L382 0 C346 90 322 300 330 476 L0 476 Z" fill="var(--navy)"/>
  </svg>

  <div class="back-brand">
    <span class="partner-badge"></span>
    <div class="chapter-name">
      <span class="chapter-name__rule"></span>
      <div>
        <p class="chapter-name__title">Eastfield State</p>
        <p class="chapter-name__sub">CHAPTER</p>
      </div>
    </div>
  </div>

  <div class="back-copy">
    <p>Join us for TWO great events at Larkmoor Golf Club in the Rochester area this June! On June 1st, The Annual Vascular Crew Roundtable (QRP), a unique all-day academic event designed to enhance current knowledge about the etiology, prevention, intervention and management of vascular disease that's now in its 11th year, will take place at the Larkmoor Golf Club in Pittsford, NY. Following the QRP Roundtable, the Eastfield</p>
    <p>Chapter of the ZQOLM will host The Second Annual Summer Soirée for all members and friends of ZQOLM. Be sure to save the date! Questions? Call (212) 555-0147 or send us an</p>
    <p>email at ask@zq-olm.example<br>Recommended lodging: The Aldercrest Lodge<br>Brightwater Rochester Hotel &amp; Spa</p>
  </div>

  <p class="back-url">www.ZQ-OLM.example/12thAnnualQRP</p>

  <div class="stamp-box" aria-label="Postage stamp area"></div>
  <span class="address-line" style="top:216px"></span>
  <span class="address-line" style="top:243px"></span>
  <span class="address-line" style="top:270px"></span>
  <span class="address-line" style="top:302px"></span>
</section>

</body>
</html>
```